Your After-Split Lantern: Sensible, Everyday Guidance for the Freshly Solo

I need a wraparound book cover design for a ~132-page workbook. Trim size will be 8.5x11 and the book will be on 60# paper. The name of this project is the name and subtitle of the book. Here's the synopsis I've come up with, which should be included on the back cover (without the quote marks):
"So you're divorced. What do you do now? There are probably a whole bunch of
things you never thought of, like:
- Cleaning up and automating your finances
- Making sure your insurance coverages are all correct
- Removing your former spouse's name from your assets and liabilities
- Building your personal team of financial advisors
Are you aware you need to take care of these things, but you don't know where to
start? This workbook is perfect for you. You'll be led, step by step, through detailed
explanations of how to do everything on this list, and much, much more!"
Here's the author bio for the back cover:
"Gregory T. Halvorsen, Esq. graduated from Brantwell College School of Law in 2002 and has been a practicing trial lawyer in the Metro Atlanta area ever since. Family law has always been a big part of Greg's practice. Throughout his career, Greg has helped hundreds of people through their divorce cases, and now through this book, Greg looks forward to being able to help them after the dust settles."
I have an ISBN bar code ready to go, so leave space for it on the back cover in the bottom right corner (winner will be expected to add the bar code graphic to the finished product).
This will be a print-on-demand book through Quillora's PressNest. They have a sizing template if you want to grab it for yourself.
Target Market(s)
Primarily divorced women, especially middle-aged and older

```html
<!DOCTYPE html>
<html lang="en">
<head>
<meta charset="utf-8">
<title>Your After-Split Lantern – Wraparound Cover</title>
<link rel="stylesheet" href="https://fonts.googleapis.com/css2?family=Anton&family=Didact+Gothic&display=swap">
<style>
  :root {
    --brick: #bd4f39;
    --maroon: #541314;
    --butter: #f7ee9c;
    --orange: #d36c2b;
    --ink: #111111;
    --white: #ffffff;
    --art-a: #8c9b5e;
    --art-b: #6b4a3a;
  }
  html, body {
    margin: 0;
    padding: 0;
    overflow: hidden;
    background: var(--brick);
  }
  .cover {
    position: relative;
    width: 1200px;
    height: 802px;
    overflow: hidden;
    background: var(--brick);
    font-family: "Didact Gothic", "Century Gothic", sans-serif;
  }
  /* Back cover */
  .back-blurb {
    position: absolute;
    left: 25px;
    top: 85px;
    width: 538px;
    height: 284px;
  }
  .back-blurb svg { position: absolute; inset: 0; }
  .blurb-text {
    position: absolute;
    left: 72px;
    top: 60px;
    margin: 0;
    color: var(--white);
    font-size: 12.4px;
    line-height: 16px;
    white-space: pre;
    font-weight: 700;
    letter-spacing: 0.1px;
  }
  .author-bio {
    position: absolute;
    left: 0;
    top: 442px;
    width: 369px;
    height: 264px;
    background: var(--butter);
  }
  .author-bio p {
    margin: 0;
    position: absolute;
    left: 36px;
    top: 54px;
    color: var(--ink);
    font-size: 12.4px;
    line-height: 16px;
    white-space: pre;
    font-weight: 700;
  }
  /* Spine */
  .spine-title, .spine-author {
    position: absolute;
    left: 593px;
    writing-mode: vertical-rl;
    color: var(--white);
    font-size: 11.6px;
    font-weight: 700;
    letter-spacing: 0.2px;
    white-space: nowrap;
  }
  .spine-title { top: 48px; }
  .spine-author { top: 640px; }
  /* Front cover */
  .front {
    position: absolute;
    left: 612px;
    top: 0;
    width: 588px;
    height: 710px;
    background: var(--butter);
  }
  .front-title {
    position: absolute;
    left: 0;
    top: 42px;
    width: 588px;
    margin: 0;
    text-align: center;
    font-family: "Anton", "Impact", sans-serif;
    font-weight: 400;
    color: var(--orange);
    font-size: 54px;
    line-height: 68px;
    letter-spacing: 0.5px;
    text-shadow: 1px 1px 1px rgba(90, 40, 10, 0.45);
  }
  .front-subtitle {
    position: absolute;
    left: 0;
    top: 186px;
    width: 588px;
    margin: 0;
    text-align: center;
    font-family: "Anton", "Impact", sans-serif;
    font-weight: 400;
    color: var(--white);
    font-size: 43px;
    line-height: 56px;
    text-shadow: 3px 3px 3px rgba(60, 40, 20, 0.7);
  }
  .front-art {
    position: absolute;
    left: 64px;
    top: 316px;
    width: 460px;
    height: 348px;
    border-radius: 14px;
    background: linear-gradient(135deg, var(--art-a), var(--art-b));
    opacity: 0.55;
  }
  .front-author {
    position: absolute;
    left: 612px;
    top: 710px;
    width: 588px;
    height: 92px;
    margin: 0;
    text-align: center;
    line-height: 92px;
    color: var(--white);
    font-size: 40px;
    font-weight: 700;
    letter-spacing: 1px;
  }
</style>
</head>
<body>
<main class="cover">
  <section class="back-cover">
    <div class="back-blurb">
      <svg width="538" height="284" viewBox="0 0 538 284" aria-hidden="true">
        <ellipse cx="269" cy="142" rx="269" ry="142" fill="var(--maroon)"/>
      </svg>
      <p class="blurb-text">"So you're divorced. What do you do now? There are probably
 a whole bunch of things you never thought of, like:
- Cleaning up and automating your finances
- Making sure your insurance coverages are all correct
- Removing your former spouse's name from your assets and liabilities
- Building your personal team of financial advisors
Are you aware you need to take care of these things, but you don't
know where to start? This workbook is perfect for you. You'll be led,
 step by step, through detailed explanations of how to do everything
 on this list, and much, much more!</p>
    </div>
    <div class="author-bio">
      <p>Gregory T. Halvorsen, Esq. graduated from Brantwell
College School of Law in 2002 and has been
 a practicing trial lawyer in the Metro Atlanta
area ever since. Family law has always been a big
part of Greg's practice. Throughout his career,
Greg has helped hundreds of people through their
 divorce cases, and now through this book, Greg
looks forward to being able to help them after
the dust settles.</p>
    </div>
  </section>

  <div class="spine-title">Your After-Split Lantern: Sensible, Everyday Guidance for the Freshly Solo</div>
  <div class="spine-author">Gregory T. Halvorsen</div>

  <section class="front">
    <h1 class="front-title">YOUR AFTER-SPLIT<br>LANTERN:</h1>
    <h2 class="front-subtitle">Sensible, Everyday Guidance<br>for the Freshly Solo</h2>
    <div class="front-art" role="img" aria-label="Illustration of a woman and a man each carrying half of a split house over their heads, walking apart"></div>
  </section>
  <p class="front-author">Gregory T. Halvorsen</p>
</main>
</body>
</html>
```